Signage for a foam car wash facility

We need signages done for a foam car wash.
We use only premium, environment-friendly, biodegradable foam wash and cleaning products.
We are in a commercial center (mall) situated in an upscale part of town and need our signage to reflect that.
We need signages for directions (two or three smaller ones), one showing that we are here, and at the actual car wash.
We will provide our logo, the texts, some pictures of the actual location the dimensions of the signages.
We need the signages to be informative, clean, crisp, modern with the use of icons if possible and some colour so that we get the attention of clients passing -by without being too flashy.
Directions to the car wash should look like a petal of a flower directing towards the car wash

Target Market(s)

Upscale market with a school and a gym next to it. Mom and dad's dropping their children at school, offices nearby.

Industry/Entity Type

Car Wash

Requirements
Nice to have
• icons, some colors,Directions to the car wash should look like a petal of a flower directing towards the car wash

```html
<!DOCTYPE html>
<html lang="en">
<head>
<meta charset="utf-8">
<title>Verida Foam Car Wash – Signage Set</title>
<link href="https://fonts.googleapis.com/css2?family=Lexend:wght@500;600&display=swap" rel="stylesheet">
<style>
  :root {
    --teal: #72c3a0;
    --lime: #b9cb3a;
    --forest: #214d3e;
    --white: #ffffff;
  }
  html, body {
    margin: 0;
    width: 1200px;
    height: 600px;
    overflow: hidden;
    background: var(--white);
  }
  .signage-sheet {
    display: block;
    width: 1200px;
    height: 600px;
    font-family: "Lexend", "Montserrat", sans-serif;
  }
  .theme-light {
    --bg: var(--white);
    --frame: var(--teal);
    --panel: var(--white);
    --mark-dot: var(--lime);
    --mark-name: var(--lime);
    --tagline: var(--teal);
    --headline: var(--teal);
    --label: var(--teal);
    --accent: var(--teal);
    --icon: var(--lime);
    --icon-detail: var(--white);
  }
  .theme-dark {
    --bg: var(--forest);
    --frame: var(--white);
    --panel: var(--teal);
    --mark-dot: var(--forest);
    --mark-name: var(--white);
    --tagline: var(--forest);
    --headline: var(--white);
    --label: var(--white);
    --accent: var(--forest);
    --icon: var(--forest);
    --icon-detail: var(--teal);
  }
  .sheet-bg { fill: var(--bg); }
  .size-label {
    fill: var(--label);
    font-size: 10px;
    font-weight: 500;
    letter-spacing: 1px;
  }
  .sign-panel { fill: var(--panel); stroke: var(--frame); }
  .brand-dot { fill: var(--mark-dot); }
  .brand-name { fill: var(--mark-name); font-weight: 600; }
  .brand-tagline { fill: var(--tagline); font-weight: 500; }
  .tagline-rule { stroke: var(--tagline); stroke-width: 2; }
  .headline { fill: var(--headline); font-weight: 600; }
  .petal-arrow { fill: var(--accent); }
  .bay-number { fill: var(--accent); }
  .bay-number-text { fill: var(--panel); font-size: 11px; font-weight: 600; }
  .vacuum-icon { fill: var(--icon); }
  .vacuum-hose { fill: none; stroke: var(--icon); stroke-width: 2.5; stroke-linecap: round; }
  .vacuum-wheel { fill: none; stroke: var(--icon-detail); stroke-width: 1.2; }
</style>
</head>
<body>
<svg class="signage-sheet" viewBox="0 0 1200 600" xmlns="http://www.w3.org/2000/svg" role="img" aria-label="Verida foam car wash signage set in light and dark colourways">
  <defs>
    <g id="signage-set">
      <rect class="sheet-bg" x="0" y="0" width="600" height="600"/>

      <!-- Main sign 244x120cm -->
      <g class="main-sign">
        <rect class="sign-panel" x="11" y="11" width="578" height="278" rx="22" stroke-width="9"/>
        <text class="size-label" x="36" y="40">244x120cm MAIN SIGN</text>
        <circle class="brand-dot" cx="86" cy="105" r="40"/>
        <text class="brand-name" x="160" y="114" font-size="70" textLength="398" lengthAdjust="spacing">VERIDA</text>
        <line class="tagline-rule" x1="160" y1="139" x2="238" y2="139"/>
        <text class="brand-tagline" x="359" y="147" font-size="22" text-anchor="middle" letter-spacing="8">PURE.SHINE</text>
        <line class="tagline-rule" x1="480" y1="139" x2="558" y2="139"/>
        <text class="headline" x="41" y="254" font-size="59" textLength="518" lengthAdjust="spacingAndGlyphs">FOAM CAR WASH</text>
      </g>

      <!-- Parking signs 150x20cm -->
      <g class="parking-signs">
        <text class="size-label" x="8" y="320">150x20cm PARKING SIGNS FOR DRY CLEAN AREA</text>

        <g class="parking-sign">
          <rect class="sign-panel" x="8.5" y="329.5" width="361" height="42" rx="12" stroke-width="4"/>
          <circle class="brand-dot" cx="29" cy="350.5" r="13"/>
          <text class="headline" x="53" y="361" font-size="28" textLength="272" lengthAdjust="spacingAndGlyphs">INTERIOR CLEANING</text>
          <g class="vacuum">
            <path class="vacuum-hose" d="M340 368 V341 a5 5 0 0 1 10 0 V345"/>
            <rect class="vacuum-icon" x="346" y="345" width="15" height="22" rx="4"/>
            <circle class="vacuum-wheel" cx="352" cy="361" r="3"/>
            <rect class="vacuum-icon" x="335" y="366.5" width="12" height="2" rx="1"/>
          </g>
        </g>

        <g class="parking-sign">
          <rect class="sign-panel" x="8.5" y="381.5" width="361" height="42" rx="12" stroke-width="4"/>
          <circle class="brand-dot" cx="29" cy="402.5" r="13"/>
          <text class="headline" x="48" y="413" font-size="28" textLength="260" lengthAdjust="spacingAndGlyphs">INTERIOR CLEANING</text>
          <circle class="bay-number" cx="323" cy="402" r="9"/>
          <text class="bay-number-text" x="323" y="406" text-anchor="middle">1</text>
          <g class="vacuum">
            <path class="vacuum-hose" d="M340 420 V393 a5 5 0 0 1 10 0 V397"/>
            <rect class="vacuum-icon" x="346" y="397" width="15" height="22" rx="4"/>
            <circle class="vacuum-wheel" cx="352" cy="413" r="3"/>
            <rect class="vacuum-icon" x="335" y="418.5" width="12" height="2" rx="1"/>
          </g>
        </g>
      </g>

      <!-- Arrow signs 40x20cm -->
      <g class="arrow-signs">
        <text class="size-label" x="592" y="320" text-anchor="end">40x20cm ARROW SIGNS</text>

        <g class="arrow-sign arrow-right">
          <rect class="sign-panel" x="497" y="329" width="93" height="44" rx="3" stroke-width="3"/>
          <circle class="brand-dot" cx="526" cy="344" r="9"/>
          <text class="brand-name" x="525" y="366" font-size="9" text-anchor="middle">VERIDA</text>
          <text class="brand-tagline" x="525" y="370.5" font-size="3.5" text-anchor="middle" letter-spacing="0.8">PURE.SHINE</text>
          <path class="petal-arrow" d="M556 344 Q556 334 565 338 L582 347 Q587 350 582 353 L565 362 Q556 366 556 356 Z"/>
        </g>

        <g class="arrow-sign arrow-left">
          <rect class="sign-panel" x="497" y="386" width="93" height="44" rx="3" stroke-width="3"/>
          <path class="petal-arrow" d="M533 401 Q533 391 524 395 L507 404 Q502 407 507 410 L524 419 Q533 423 533 413 Z"/>
          <circle class="brand-dot" cx="561" cy="401" r="9"/>
          <text class="brand-name" x="560" y="423" font-size="9" text-anchor="middle">VERIDA</text>
          <text class="brand-tagline" x="560" y="427.5" font-size="3.5" text-anchor="middle" letter-spacing="0.8">PURE.SHINE</text>
        </g>
      </g>

      <!-- Wash bay sign 200x50cm -->
      <g class="wash-bay-sign">
        <text class="size-label" x="8" y="461">200x50cm WASH BAY SIGN</text>
        <rect class="sign-panel" x="9.5" y="472" width="480" height="111" rx="8" stroke-width="6"/>
        <circle class="brand-dot" cx="101" cy="511" r="23"/>
        <text class="brand-name" x="101" y="564" font-size="22" text-anchor="middle" textLength="115" lengthAdjust="spacing">VERIDA</text>
        <line class="tagline-rule" x1="43" y1="570" x2="65" y2="570" style="stroke-width:1"/>
        <text class="brand-tagline" x="101" y="572.5" font-size="7" text-anchor="middle" letter-spacing="2">PURE.SHINE</text>
        <line class="tagline-rule" x1="137" y1="570" x2="159" y2="570" style="stroke-width:1"/>
        <text class="headline" x="189" y="545" font-size="49" textLength="270" lengthAdjust="spacingAndGlyphs">WASH BAY</text>
      </g>
    </g>
  </defs>

  <use href="#signage-set" class="theme-light" x="0" y="0"/>
  <use href="#signage-set" class="theme-dark" x="600" y="0"/>
</svg>
</body>
</html>
```